Healthy Vending Machine Business Flyer

A modorn design that represents our healthy vending machine business. We will attach a picture of the machine we want on the flyer along with our logo. We will also upload the wording we want on the flyer

Colors

Designer to choose colors to be used in the design.

Requirements
Must have
• Flyer wording
• Front of flyer:
• (Picture of vending machine on the front)
• Free healthy vending machines hit the Treasure Valley
• Keep your Employees happy & productive with healthy vending options at work
• • No Cost to Your Company
• • Remote tracking tells us when your favorite snacks are running low
• • Credit Card/Smartphone Payment Technology
• • Ability to Customize your Snacks and Drinks
• • Locally Owned and Operated
• • Delicious Healthy Options
• Back of flyer:
• 431 Crispleaf Vending is a locally owned and operated company dedicated to making healthy snacks and drinks easily available for the Treasure Valley. We provide the latest in vending machine technology accepting credit cards, tillo wallet, and norvex wallet. State of the art inventory tracking tells us when your machine is running low so you're never out of your favorite drink or snack. We offer flexible stocking based on your companies needs and work with you on what items you want in the machine. Our goal is to give your employees and clients healthy options on the go
• To be considered for this FREE service for your business please visit: 431crispleafvending.com
• Or call/email today:
• Phone: 431-555-0162
• Email: 431crispleafvending@mailtrove.com
Should not have
• Any Additional Fruit images besides what is on the machine image.

```html
<!DOCTYPE html>
<html lang="en">
<head>
<meta charset="utf-8">
<title>431 Crispleaf Vending – Flyer</title>
<link href="https://fonts.googleapis.com/css2?family=Rubik:wght@500;700&family=Raleway:wght@500;700&display=swap" rel="stylesheet">
<style>
  :root{
    --backdrop:#7a7a7a;
    --mint-light:#f3fbf1;
    --mint:#d6f0d0;
    --panel:rgba(255,255,255,0.78);
    --ink:#2b2b2b;
    --green:#3f9a12;
    --orange:#f28a12;
    --machine-dark:#1e1a18;
    --machine-red:#b8322a;
    --machine-green:#6a9a2a;
  }
  *{box-sizing:border-box;margin:0;padding:0}
  html,body{width:1200px;height:478px;overflow:hidden}
  body{background:var(--backdrop);position:relative;font-family:"Rubik",sans-serif;color:var(--ink)}
  .flyer{position:absolute;top:46px;width:544px;height:386px;overflow:hidden;
    background:radial-gradient(circle at 80% 30%,var(--mint) 0%,var(--mint-light) 55%,#ffffff 100%)}
  .flyer--front{left:46px}
  .flyer--back{left:610px}
  .text-panel{position:absolute;left:0;top:0;width:258px;height:386px;background:var(--panel)}
  .machine{position:absolute;left:302px;top:16px;width:180px;height:362px;
    background:linear-gradient(160deg,var(--machine-dark) 0%,var(--machine-red) 45%,var(--machine-green) 75%,var(--machine-dark) 100%);
    border-radius:2px;box-shadow:4px 6px 10px rgba(0,0,0,0.25)}
  .brand{position:absolute;left:30px;top:92px;display:flex;align-items:center;gap:7px;
    font-family:"Rubik",sans-serif;font-weight:700;font-size:19px;color:var(--orange);white-space:nowrap}
  .brand__dot{width:12px;height:12px;border-radius:50%;background:var(--green);flex:none}
  .headline{position:absolute;left:30px;top:138px;width:230px;font-weight:700;font-size:19.5px;line-height:22px;color:var(--ink)}
  .subhead{position:absolute;left:30px;top:214px;width:220px;font-weight:700;font-size:11.6px;line-height:13.5px;color:var(--green)}
  .benefits{position:absolute;left:30px;top:272px;list-style:none;font-weight:500;font-size:8.3px;line-height:10.3px;color:var(--ink)}
  .benefits li{display:flex;gap:5px;margin-bottom:3.3px;width:228px}
  .benefits svg{flex:none;margin-top:1px}
  .about{position:absolute;left:30px;top:136px;width:182px;font-family:"Raleway",sans-serif;font-weight:500;font-size:7.4px;line-height:9.8px;color:var(--ink)}
  .cta{position:absolute;left:30px;top:266px;width:172px;font-family:"Raleway",sans-serif;font-weight:700;font-size:9.2px;line-height:11.5px;color:var(--green)}
  .web{position:absolute;left:30px;top:294px;font-weight:700;font-size:12.3px;color:var(--green)}
  .call{position:absolute;left:30px;top:318px;font-family:"Raleway",sans-serif;font-weight:700;font-size:9.2px;color:var(--green)}
  .phone{position:absolute;left:30px;top:331px;font-weight:700;font-size:14.5px;color:var(--green)}
  .email{position:absolute;left:30px;top:351px;font-weight:700;font-size:9.5px;color:var(--green)}
</style>
</head>
<body>

<section class="flyer flyer--front">
  <div class="text-panel"></div>
  <div class="machine" role="img" aria-label="Photo of the healthy vending machine with snack and drink shelves and a fruit-printed wrap"></div>

  <div class="brand"><span class="brand__dot"></span>431 Crispleaf Vending</div>
  <h1 class="headline">Free healthy vending machines hit the Treasure Valley</h1>
  <h2 class="subhead">Keep Your Employees Happy &amp; Productive With Healthy Vending Options At Work</h2>
  <ul class="benefits">
    <li><svg width="8" height="8" viewBox="0 0 10 10"><circle cx="5" cy="5" r="4.3" fill="none" stroke="#2b2b2b" stroke-width="1"/><path d="M3 5.2 4.5 6.6 7.2 3.6" fill="none" stroke="#2b2b2b" stroke-width="1.1"/></svg>No Cost to Your Company</li>
    <li><svg width="8" height="8" viewBox="0 0 10 10"><circle cx="5" cy="5" r="4.3" fill="none" stroke="#2b2b2b" stroke-width="1"/><path d="M3 5.2 4.5 6.6 7.2 3.6" fill="none" stroke="#2b2b2b" stroke-width="1.1"/></svg>Remote tracking tells us when your favorite<br>snacks are running low</li>
    <li><svg width="8" height="8" viewBox="0 0 10 10"><circle cx="5" cy="5" r="4.3" fill="none" stroke="#2b2b2b" stroke-width="1"/><path d="M3 5.2 4.5 6.6 7.2 3.6" fill="none" stroke="#2b2b2b" stroke-width="1.1"/></svg>Credit Card/Smartphone Payment Technology</li>
    <li><svg width="8" height="8" viewBox="0 0 10 10"><circle cx="5" cy="5" r="4.3" fill="none" stroke="#2b2b2b" stroke-width="1"/><path d="M3 5.2 4.5 6.6 7.2 3.6" fill="none" stroke="#2b2b2b" stroke-width="1.1"/></svg>Ability to Customize your Snacks and Drinks</li>
    <li><svg width="8" height="8" viewBox="0 0 10 10"><circle cx="5" cy="5" r="4.3" fill="none" stroke="#2b2b2b" stroke-width="1"/><path d="M3 5.2 4.5 6.6 7.2 3.6" fill="none" stroke="#2b2b2b" stroke-width="1.1"/></svg>Locally Owned and Operated</li>
    <li><svg width="8" height="8" viewBox="0 0 10 10"><circle cx="5" cy="5" r="4.3" fill="none" stroke="#2b2b2b" stroke-width="1"/><path d="M3 5.2 4.5 6.6 7.2 3.6" fill="none" stroke="#2b2b2b" stroke-width="1.1"/></svg>Delicious Healthy Options</li>
  </ul>
</section>

<section class="flyer flyer--back">
  <div class="text-panel"></div>
  <div class="machine" role="img" aria-label="Photo of the healthy vending machine with snack and drink shelves and a fruit-printed wrap"></div>

  <div class="brand"><span class="brand__dot"></span>431 Crispleaf Vending</div>
  <p class="about">431 Crispleaf Vending is a locally owned and operated company dedicated to making healthy snacks and drinks easily available for the Treasure Valley. We provide the latest in vending machine technology accepting credit cards, tillo wallet, and norvex wallet. State of the art inventory tracking tells us when your machine is running low so you're never out of your favorite drink or snack. We offer flexible stocking based on your companies needs and work with you on what items you want in the machine. Our goal is to give your employees and clients healthy options on the go.</p>
  <p class="cta">To be considered for this FREE service for your business please visit:</p>
  <p class="web">www.431crispleafvending.com</p>
  <p class="call">Or call/email today:</p>
  <p class="phone">Ph: 431-555-0162</p>
  <p class="email">Email: 431crispleafvending@mailtrove.com</p>
</section>

</body>
</html>
```